Business Card Design

My business is writing crime novels to entertain readers. I write legal thrillers and mysteries. I need a card for publishers, agents, other authors, and media.

Industry/Entity Type

Legal

Contact Information for Business Card

Paul Ostrander
www.ostranderthrillers.example
paulbostrander@mailbox.example
0064 27 5139427

```html
<!DOCTYPE html>
<html lang="en">
<head>
<meta charset="utf-8">
<title>Paul Ostrander – Business Card</title>
<link rel="stylesheet" href="https://fonts.googleapis.com/css2?family=Exo+2:wght@400;500;600&display=swap">
<style>
  :root {
    --backdrop: #d9d9db;
    --card: #fbfbfb;
    --ink: #3b3f9a;
    --rule: #4a4fae;
    --photo-light: #8a8a8a;
    --photo-dark: #5f5f61;
  }
  * { margin: 0; padding: 0; box-sizing: border-box; }
  html, body {
    width: 1200px;
    height: 864px;
    overflow: hidden;
    background: var(--backdrop);
    font-family: "Exo 2", "Titillium Web", sans-serif;
  }
  .card {
    position: absolute;
    left: 110px;
    top: 152px;
    width: 980px;
    height: 560px;
    background: var(--card);
    box-shadow: 0 6px 24px rgba(0,0,0,0.18);
  }
  .rule { position: absolute; background: var(--rule); }
  .rule--top { left: 70px; top: 95px; width: 760px; height: 1.5px; }
  .rule--bottom { left: 120px; top: 480px; width: 790px; height: 1.5px; }
  .rule--divider { left: 480px; top: 150px; width: 1.5px; height: 250px; }
  .portrait {
    position: absolute;
    left: 120px;
    top: 145px;
    width: 290px;
    height: 285px;
    border: 2px solid var(--ink);
    background: radial-gradient(circle at 50% 40%, var(--photo-light), var(--photo-dark));
  }
  .identity { position: absolute; left: 565px; top: 140px; color: var(--ink); }
  .identity__name { font-size: 36px; font-weight: 500; letter-spacing: 0.5px; line-height: 1.1; }
  .identity__role { font-size: 20px; font-weight: 600; margin-left: 5px; margin-top: 2px; }
  .contacts { position: absolute; left: 565px; top: 318px; list-style: none; color: var(--ink); }
  .contacts__item { display: flex; align-items: center; height: 40px; font-size: 22px; letter-spacing: 0.8px; }
  .contacts__icon { width: 22px; height: 22px; margin-right: 16px; flex: none; }
</style>
</head>
<body>
  <main class="card">
    <div class="rule rule--top"></div>
    <div class="portrait" role="img" aria-label="Portrait photograph of the author"></div>
    <div class="rule rule--divider"></div>
    <header class="identity">
      <h1 class="identity__name">PAUL OSTRANDER</h1>
      <p class="identity__role">OWANER</p>
    </header>
    <ul class="contacts">
      <li class="contacts__item">
        <svg class="contacts__icon" viewBox="0 0 22 22" aria-hidden="true">
          <rect x="6" y="2" width="10" height="18" rx="2" fill="none" stroke="#3b3f9a" stroke-width="1.8"/>
          <line x1="9" y1="17" x2="13" y2="17" stroke="#3b3f9a" stroke-width="1.5"/>
        </svg>
        0064 27 5139427
      </li>
      <li class="contacts__item">
        <svg class="contacts__icon" viewBox="0 0 22 22" aria-hidden="true">
          <rect x="2" y="4" width="18" height="12" fill="none" stroke="#3b3f9a" stroke-width="1.8"/>
          <line x1="11" y1="16" x2="11" y2="19" stroke="#3b3f9a" stroke-width="1.8"/>
          <line x1="7" y1="19.5" x2="15" y2="19.5" stroke="#3b3f9a" stroke-width="1.8"/>
        </svg>
        www.ostranderthrillers.example
      </li>
      <li class="contacts__item">
        <svg class="contacts__icon" viewBox="0 0 22 22" aria-hidden="true">
          <rect x="2" y="5" width="18" height="13" fill="#3b3f9a"/>
          <polyline points="2,5 11,12 20,5" fill="none" stroke="#fbfbfb" stroke-width="1.4"/>
          <line x1="2" y1="18" x2="9" y2="11" stroke="#fbfbfb" stroke-width="1"/>
          <line x1="20" y1="18" x2="13" y2="11" stroke="#fbfbfb" stroke-width="1"/>
        </svg>
        paulbostrander@mailbox.example
      </li>
    </ul>
    <div class="rule rule--bottom"></div>
  </main>
</body>
</html>
```